glow 482 is renewing its image

more dynamic website, make it look more attractive for the services we offer, at the same time more accurate on the services description. We want people to know we offer treatments that big corporations offer but not as expensive as they offer it. prices will be add by me once the website is approve

already have a website with SiteBuilder www.glow482skin.com

Target Market(s)

women between 21 to 75

Industry/Entity Type

beauty services, body contouring

Colors

Designer to choose colors to be used in the design.

Requirements
Must have
• pictures of treatments
Nice to have
• accurate information about treatmnets, treatments menu
Should not have
• no online shopping

```html
<!DOCTYPE html>
<html lang="en">
<head>
<meta charset="utf-8">
<title>glow 482 – website pages</title>
<link href="https://fonts.googleapis.com/css2?family=Roboto:wght@300;400;500;700&display=swap" rel="stylesheet">
<style>
:root{
  --canvas:#f1f1f1;
  --page:#ffffff;
  --gold:#c9975f;
  --gold-soft:#d6a977;
  --brown:#7b4a1e;
  --sand:#f0e2d6;
  --grey-text:#b8b8b8;
  --note:#cfcfcf;
  --black:#000000;
}
*{margin:0;padding:0;box-sizing:border-box}
html,body{width:1200px;height:2692px;overflow:hidden}
body{background:var(--canvas);font-family:"Roboto",Arial,sans-serif;position:relative}
.spec-note{position:absolute;left:56px;color:var(--note);font-size:13px;font-weight:300;white-space:nowrap;transform-origin:0 0;transform:rotate(90deg)}
.page{position:absolute;left:116px;width:969px;background:var(--page);box-shadow:0 2px 10px rgba(0,0,0,.12);overflow:hidden}
.page--treatment{top:122px;height:1661px}
.page--about{top:1843px;height:726px}
.nav a{position:absolute;top:92px;font-size:13px;color:var(--gold);text-decoration:none;letter-spacing:.2px}
.nav a.is-active{color:var(--brown);font-weight:700}
.social{position:absolute;top:91px;width:17px;height:17px;border-radius:50%;background:var(--brown)}
.dropdown{position:absolute;left:674px;top:117px;width:110px;height:65px;background:var(--brown);padding:12px 12px;z-index:2}
.dropdown span{display:block;color:#fff;font-size:13px;line-height:24px}
.rule{position:absolute;left:0;width:100%;height:3px;background:var(--gold-soft)}
.hero{position:absolute;left:0;width:100%}
.hero--treatment{top:168px;height:441px;background:linear-gradient(100deg,#e9e9ea 0%,#f4f1ee 35%,#d9b49a 60%,#f3ece7 85%,#fbfbfb 100%)}
.hero--about{top:166px;height:443px;background:radial-gradient(circle at 25% 30%,#e8d3bf 0,#f2e4d6 30%,transparent 55%),linear-gradient(90deg,#f3e6d9 0%,#f6ece3 45%,#e7d1bd 80%,#d9bca1 100%)}
.brand{position:absolute;display:flex;align-items:center;gap:12px;color:var(--brown);font-weight:500;white-space:nowrap}
.brand .dot{width:14px;height:14px;border-radius:50%;background:var(--brown)}
.brand--hero{left:700px;top:262px;font-size:40px}
.brand--about{left:150px;top:397px;font-size:48px}
.title{position:absolute;left:0;width:100%;text-align:center;top:654px;font-size:28px;font-weight:700;color:var(--brown)}
.subtitle{position:absolute;left:0;width:100%;text-align:center;top:697px;font-size:25px;line-height:34px;font-weight:500;color:var(--gold)}
.body-copy{position:absolute;left:111px;width:743px;top:791px}
.body-copy p{font-size:10.5px;line-height:19.6px;color:var(--grey-text);margin-bottom:19.6px;font-weight:400}
.btn{position:absolute;display:flex;align-items:center;justify-content:center;font-size:14px;color:#fff}
.btn--pdf{left:698px;top:1109px;width:154px;height:44px;background:var(--gold-soft);font-size:14px}
.footer{position:absolute;left:0;top:1213px;width:100%;height:448px;background:var(--sand)}
.footer h3{position:absolute;font-size:14px;font-weight:700;color:var(--brown)}
.contact-list{position:absolute;left:111px;top:78px;list-style:none}
.contact-list li{font-size:14px;color:var(--gold);line-height:35.5px}
.about-text{position:absolute;left:489px;top:74px;width:366px}
.about-text p{font-size:11px;line-height:17px;color:var(--gold);margin-bottom:17px}
.btn--policy{left:111px;top:278px;width:367px;height:44px;background:var(--brown);font-size:13.5px}
.btn--policy b{font-weight:500;margin-left:4px}
.copyright{position:absolute;left:111px;top:352px;font-size:9.5px;color:var(--brown)}
.copyright b{font-weight:700}
.btn--call{left:624px;top:403px;width:232px;height:45px;background:var(--black);font-size:14.5px}
.about-title{position:absolute;left:488px;top:252px;font-size:29px;font-weight:500;color:var(--brown)}
.about-panel{position:absolute;left:468px;top:303px;width:406px;height:251px;background:rgba(201,151,95,.55);padding:18px 20px}
.about-panel p{font-size:11px;line-height:19.6px;color:#fff;text-align:justify;margin-bottom:19.6px}
</style>
</head>
<body>

<div class="spec-note" style="top:420px">Width from SITEBUILDER 980px - Design within 940px by 726 px</div>
<div class="spec-note" style="top:2140px">Width from SITEBUILDER 980px - Design within 940px by 726 px</div>

<section class="page page--treatment">
  <nav class="nav">
    <a style="left:115px">HOME</a>
    <a style="left:180px">TREATMENTS</a>
    <a style="left:291px" class="is-active">POST SURGERY TREATMENTS</a>
    <a style="left:505px">CONTACT</a>
    <a style="left:588px">ABOUT US</a>
    <a style="left:678px">MORE</a>
  </nav>
  <span class="social" style="left:798px"></span>
  <span class="social" style="left:845px"></span>
  <div class="dropdown"><span>LIST ITEMS</span><span>COURSES</span></div>
  <div class="rule" style="top:149px"></div>

  <div class="hero hero--treatment" role="img" aria-label="Photo of a specialist giving a post-surgery body treatment with a device to a client lying down"></div>
  <div class="brand brand--hero"><span class="dot"></span>glow 482</div>

  <h1 class="title">Post-surgery Treatment</h1>
  <h2 class="subtitle">(Post Surgery, Pre &amp; Post Liposuction, Tummy Tuck,<br>Mammoplasty, Neck Lift, Breast Implant)</h2>

  <div class="body-copy">
    <p>The post-surgery treatment is a combination of techniques that speed up the patient's healing process after surgery. Its main objective is to eliminate the surgery's inflammation and correct the skin irregularities produced by Fibrosis.</p>
    <p>Fibrosis is an effect suffered by most patients after surgery. If the patient notices hardening of the skin tissues, lumps or deformations in the area that was subjected to surgery, then there is Fibrosis and post-surgery treatment is then needed.</p>
    <p>The application of the post-surgery treatment will depend on the patient's medical condition and will be administered according to the evaluation of our specialists who recommend that this treatment begin three to five days after surgery.</p>
    <p>glow 482 Skin Lounge After Lipo Massage is a specialized center in post liposuction treatment (Tummy Tuck, Mammoplasty, Neck Lift, Breast Implant) using a combination of Lymphatic Drainage, Ultrasound, Ultra Cavitation, Vacuum Therapy,</p>
    <p>Electro stimulation techniques among others.</p>
  </div>

  <div class="btn btn--pdf">download PDF</div>

  <footer class="footer">
    <h3 style="left:111px;top:52px">CONTACT US</h3>
    <ul class="contact-list">
      <li>a.&nbsp; 18 Alder Court Westbrook CT 06099</li>
      <li>e.&nbsp; glow482spa@mailbox.com</li>
      <li>t.&nbsp; (860) 555-0142 or (860) 555-0187</li>
    </ul>
    <h3 style="left:489px;top:50px">MORE ABOUT US</h3>
    <div class="about-text">
      <p>At glow 482 Skin Lounge we provide high quality skin and body treatments that will make you look great and feel great!</p>
      <p>With more than 10 years of experience our Esthetician Marisa will provide you with the information and the treatment that is right for you and your budget.</p>
      <p>We are like your personal assistants but for your beauty. You can always call us if you have any questions.</p>
    </div>
    <div class="btn btn--policy">Please read our<b>Reservation &amp; Cancellation Policy.</b></div>
    <p class="copyright">© 2021 by <b>Skin Care Co</b>. Proudly created with SiteBuilder</p>
    <div class="btn btn--call">If we take too long, CALL US!</div>
  </footer>
</section>

<section class="page page--about">
  <nav class="nav">
    <a style="left:117px">HOME</a>
    <a style="left:182px">TREATMENTS</a>
    <a style="left:293px">POST SURGERY TREATMENTS</a>
    <a style="left:502px">CONTACT</a>
    <a style="left:584px" class="is-active">ABOUT US</a>
    <a style="left:676px">MORE</a>
  </nav>
  <span class="social" style="left:798px"></span>
  <span class="social" style="left:845px"></span>
  <div class="dropdown"><span>LIST ITEMS</span><span>COURSES</span></div>
  <div class="rule" style="top:150px"></div>

  <div class="hero hero--about" role="img" aria-label="Beauty collage of skin close-ups and a woman's face in warm skin tones"></div>
  <div class="brand brand--about"><span class="dot"></span>glow 482</div>

  <h2 class="about-title">About Us</h2>
  <div class="about-panel">
    <p>You deserve more, whether it's a suite of services that treats every bodily need, a top-notch professional staff or a relaxing venue to enjoy them in. This is where We shine.</p>
    <p>Here, you can take your pick of from a variety of beauty-boosting services. We use Peruvian natural products. For instance, the Skin Care Body Wraps, which are tailored to relax the body, detoxify, exfoliate and hydrate the skin, all while helping you to lose inches. This treatments enhances both your psychological and physical wellness. Ensuring each client gets what they want is our goal.</p>
  </div>
</section>

</body>
</html>
```